Wireless retailer specializing in sale / purchase of used and refurbished devices. We are an authorized dealer for " vCarda Wireless". Logos for vCarda and our logo have been included.
Business card needs to feature both locations address. We will do a reprint once we have the phone number for the second location and remove the "coming soon" text.
Cards will also need to be personalized per employee. Will post that information as well.
Any suggestions are welcome
Industry/Entity Type
Business
Contact Information for Business Card
The Signal Hut
Brenmoor Field Plaza Shopping Center
4871 Quarrel Lane
Virginia Beach, VA 23464
757.318.9264
Coming in 2014
The Signal Hut 2
Marlow Bexby Shopping Center
2619 Tessing Rd Suite #847
Virginia Beach, VA 23452
Look and feel
Each slider illustrates characteristics of the customer's brand and the style your logo design should communicate.

```html
<!DOCTYPE html>
<html lang="en">
<head>
<meta charset="utf-8">
<title>The Signal Hut – Business Card</title>
<link rel="stylesheet" href="https://fonts.googleapis.com/css2?family=Exo+2:wght@300;400&display=swap">
<style>
  :root {
    --card-bg: #232425;
    --brand-blue: #1d5aa5;
    --text-white: #ffffff;
    --divider: #4a4b4c;
    --badge-bg: #ffffff;
  }
  html, body {
    margin: 0;
    padding: 0;
    overflow: hidden;
    background: var(--card-bg);
  }
  .card {
    position: relative;
    width: 1200px;
    height: 741px;
    background: var(--card-bg);
    font-family: "Exo 2", sans-serif;
    font-weight: 300;
    color: var(--text-white);
    overflow: hidden;
  }
  .brand-name {
    position: absolute;
    left: 132px;
    top: 184px;
    margin: 0;
    font-family: "Exo 2", sans-serif;
    font-weight: 400;
    font-size: 60px;
    line-height: 62px;
    color: var(--brand-blue);
    text-transform: uppercase;
    letter-spacing: 3px;
  }
  .partner-badge {
    position: absolute;
    left: 888px;
    top: 211px;
    width: 181px;
    height: 74px;
    border-radius: 10px;
    background: var(--badge-bg);
  }
  .location {
    position: absolute;
    top: 404px;
  }
  .location--current { left: 132px; }
  .location--upcoming { left: 676px; }
  .location-title {
    margin: 0 0 6px;
    font-weight: 300;
    font-size: 24px;
    line-height: 34px;
    color: var(--brand-blue);
    text-transform: uppercase;
  }
  .location-address {
    margin: 0;
    font-style: normal;
    font-size: 24.5px;
    line-height: 40px;
    color: var(--text-white);
  }
  .location-phone {
    margin: 14px 0 0;
    font-size: 38px;
    line-height: 46px;
    letter-spacing: 2px;
    color: var(--brand-blue);
  }
  .column-divider {
    position: absolute;
    left: 619px;
    top: 411px;
    width: 1px;
    height: 142px;
    background: var(--divider);
  }
</style>
</head>
<body>
  <main class="card">
    <h1 class="brand-name">The Signal<br>Hut</h1>

    <div class="partner-badge" role="img" aria-label="vCarda Wireless authorized retailer badge"></div>

    <section class="location location--current">
      <h2 class="location-title">The Signal Hut</h2>
      <address class="location-address">
        Brenmoor Field Plaza Shopping Center<br>
        4871 Quarrel Lane<br>
        Virginia Beach, VA 23464
      </address>
      <p class="location-phone">757.318.9264</p>
    </section>

    <div class="column-divider"></div>

    <section class="location location--upcoming">
      <h2 class="location-title">Coming in 2014</h2>
      <address class="location-address">
        Marlow Bexby Shopping Center<br>
        2619 Tessing Rd Suite #847<br>
        Virginia Beach, VA 23452
      </address>
    </section>
  </main>
</body>
</html>
```